Redesign of an educational Eye website for Medical Students and Healthcare professionals

www.corvellelearninghub.com is an educational resource, illustrated using high quality 3D animations, for undergraduate medical students and healthcare professionals to learn about the anatomy of the human eye and associated common eye disorders.

The website was originally developed (using a Joomla template) a couple of years ago and we now want to update the brand and design of the site. Example content and animations can be found at https://www.corvellelearninghub.com/overview or https://www.corvellelearninghub.com/ocular-anatomy/orbital-anatomy

We would like a new logo and home page design (to include new colour palette, fonts and updated overall design).

The attached PowerPoint contains an example layout of the revised components we want to appear on the new Home page. We plan to have a hero panel at the top of page playing a short video of some of the animations. Similar to how this site works (www.zeptal.uk.com).

We want the new site to feel Professional, Modern and Clean and simple.

Target Market(s)

Undergraduate medical students and Healthcare Professionals

Industry/Entity Type

Medical

Logo Text

Corvelle Learning Hub

Number of Pages Required

1 page

Font styles to use
Sans Serif

Colors

Designer to choose colors to be used in the design.

```html
<!DOCTYPE html>
<html lang="en">
<head>
<meta charset="utf-8">
<title>Corvelle Learning Hub – Testimonials and Free Trial</title>
<link rel="stylesheet" href="https://fonts.googleapis.com/css2?family=Jost:wght@300;400;500;700&display=swap">
<style>
  :root {
    --bar-dark: #333333;
    --page-white: #ffffff;
    --band-grey: #e8e8e8;
    --ink: #333333;
    --ink-soft: #555555;
    --ink-muted: #7a7a7a;
    --dot-off: #c8c8c8;
    --dot-on: #333333;
    --cta-blue: rgba(46, 112, 140, 0.88);
    --photo-light: #c9d6df;
    --photo-dark: #1e2328;
  }
  * { box-sizing: border-box; margin: 0; padding: 0; }
  html, body {
    width: 1200px; height: 749px; overflow: hidden;
    background: var(--page-white);
    font-family: "Jost", sans-serif;
    color: var(--ink);
  }
  .page { position: relative; width: 1200px; height: 749px; }
  .top-bar { position: absolute; left: 0; top: 0; width: 1200px; height: 12px; background: var(--bar-dark); }

  .section-title {
    position: absolute; left: 0; width: 1200px; text-align: center;
    font-weight: 400; font-size: 25px; font-variant: small-caps; letter-spacing: 0.2px;
    color: var(--ink);
  }
  .testimonials-title { top: 34px; }

  .avatar {
    position: absolute; left: 181px; top: 120px; width: 138px; height: 138px;
    border-radius: 50%; border: 1px solid #555;
    background: radial-gradient(circle at 50% 55%, #e9eef3 0%, #d5dfe8 60%, #b9c6d3 100%);
    box-shadow: 0 1px 3px rgba(0,0,0,0.25);
  }
  .testimonial { position: absolute; left: 344px; top: 114px; width: 700px; }
  .person-name {
    font-weight: 400; font-size: 24px; font-variant: small-caps; color: var(--ink);
    line-height: 30px; margin-left: 2px;
  }
  .person-role {
    font-weight: 700; font-size: 14.5px; color: var(--ink); line-height: 18px; margin-left: 2px;
  }
  .quote {
    margin-top: 7px; font-weight: 400; font-size: 13.6px; line-height: 24.2px; color: var(--ink-soft);
  }
  .slider-dots { display: flex; gap: 3px; margin-top: 7px; }
  .slider-dots span { width: 7px; height: 7px; border-radius: 50%; background: var(--dot-off); }
  .slider-dots span.active { background: var(--dot-on); }

  .trial-band { position: absolute; left: 0; top: 318px; width: 1200px; height: 415px; background: var(--band-grey); }
  .trial-title { top: 344px; }
  .trial-note {
    position: absolute; left: 0; top: 380px; width: 1200px; text-align: center;
    font-size: 13.5px; font-weight: 400; color: var(--ink-muted);
  }
  .trial-photo {
    position: absolute; left: 350px; top: 427px; width: 496px; height: 269px;
    border: 1px solid #cfcfcf;
    background: linear-gradient(135deg, #e4e9ee 0%, var(--photo-light) 38%, #6f7b86 62%, var(--photo-dark) 100%);
  }
  .trial-button {
    position: absolute; left: 474px; top: 536px; width: 248px; height: 52px;
    background: var(--cta-blue); color: #fff; text-decoration: none;
    display: flex; align-items: center; justify-content: center;
    font-weight: 500; font-size: 16px; letter-spacing: 0.2px;
  }
</style>
</head>
<body>
<div class="page">
  <div class="top-bar"></div>

  <h2 class="section-title testimonials-title">What are people saying about Corvelle Learning Hub?</h2>

  <div class="avatar" role="img" aria-label="Portrait photo of the consultant giving the testimonial"></div>
  <div class="testimonial">
    <p class="person-name">Mr Daniel Hartwell MB ChB FRCOphth</p>
    <p class="person-role">Consultant Ophthalmologist and Head of the School of Ophthalmology, Ashford Deanery NWR</p>
    <p class="quote">“What sets this website apart are the superb 3D animations which enhance the accompanying text more effectively than clinical videos or photographs. I would whole heartedly recommend it to medical students, optometrists, GP's, casualty doctors and ophthalmic nurse practitioners, both as an introduction to ophthalmology, but also to refresh their knowledge of core ophthalmic examination techniques and conditions.”</p>
    <div class="slider-dots"><span class="active"></span><span></span><span></span><span></span><span></span><span></span></div>
  </div>

  <section class="trial-band"></section>
  <h2 class="section-title trial-title">Want to try Corvelle Learning Hub for free?</h2>
  <p class="trial-note">No credit card details required. It's completely free for 3 days.</p>
  <div class="trial-photo" role="img" aria-label="Photo of hands using a laptop keyboard and mouse"></div>
  <a class="trial-button" href="#">START FREE TRIAL</a>
</div>
</body>
</html>
```